Environmental Public Service Campaign Needs a Bus Advertisement Design

We are creating advertisements to be placed inside city buses for an environmental public service campaign. With this campaign we are promoting the use of a hotline called the "Brimzel Hotline." This is a phone number citizens can call when they see people illegally dumping things into the storm drain. We want people to know what to look for and how report incidents via phone, text, or smartphone app.

A full project brief is also attached.

Target Market(s)

Residents of Harlow County, DE
Residents of the City of Fernbrook, DE

Industry/Entity Type

Campaign

Font styles to use
Serif

Requirements
Must have
• The size of the advertisement is 11"h x 28"w
• Final file format is a pdf
• Leave 1/2" on top and bottom with no graphics to allow for installation in a frame
• MUST HAVE: 1 image of the boy talking on the phone
• (images to choose from are attached)
• MUST HAVE: ALL 4 Images of Illicit Discharges- all four images to use are attached
• These images should take up a lot of space in the design
• Must have the following text:
• Header: Water pollution is a Crime. Don’t stand for it. BriMMzel!
• Info text: If you see pollution going into or out of the public sewer system, report it!
• Call or text (555) BRI-MZEL
• Email hotline@555brimzel.example or visit www.555brimzel.example
• City of Fernbrook residents can also use the Mark Up/Close Out App
• The “double P” in BRIMMZEL stands for “Prevent Pollution”
• Must have the logos of participating jurisdictions:
• Harlow County, City of Fernbrook, Korvax (logos are attached)
Nice to have
• The “P” in BriMMzel and “Prevent Pollution” made more obvious, tying the idea together that the double “P” in BriMMzel means “Prevent Pollution”
• Maybe image of water in the background of the image of people calling or texting on the phone
Should not have
• No swimming pools or bottled water images
• No images of people dumping things in the drain

```html
<!DOCTYPE html>
<html lang="en">
<head>
<meta charset="utf-8">
<title>Brimzel Hotline – Bus Advertisement</title>
<link rel="stylesheet" href="https://fonts.googleapis.com/css2?family=Roboto+Slab:wght@400;700;800;900&display=swap">
<style>
  :root {
    --backdrop: #9a9a9a;
    --alert-red: #f0253c;
    --alert-yellow: #f7c400;
    --panel-dark: #2f2f2f;
    --column-dark: #353535;
    --ghost-text: #3a3a3a;
    --white: #ffffff;
    --muted: #d2d2d2;
    --link-red: #ff3a4e;
    --runoff: #8f9a98;
    --oil: #4f5c6a;
    --clippings: #a39c84;
    --lawn: #7f9a52;
  }
  * { box-sizing: border-box; margin: 0; padding: 0; }
  html, body {
    width: 1200px; height: 573px; overflow: hidden;
    background: var(--backdrop);
  }
  .ad {
    position: absolute; left: 44px; top: 63px;
    width: 1114px; height: 432px;
    background: var(--white);
    font-family: "Roboto Slab", Georgia, serif;
    box-shadow: 0 2px 8px rgba(0,0,0,0.35);
  }

  /* Headline band */
  .headline-band {
    position: absolute; left: 0; top: 0; width: 100%; height: 78px;
    background: var(--alert-red);
    display: flex; align-items: center;
    padding-left: 104px;
  }
  .headline {
    font-weight: 700; font-size: 30px; color: var(--white);
    letter-spacing: -0.3px; white-space: nowrap;
  }
  .alert-icon { position: absolute; left: 14px; top: 10px; width: 70px; height: 70px; }

  /* Pollution photo strip */
  .photo { position: absolute; top: 82px; height: 155px; }
  .photo-runoff { left: 0; width: 224px; background: linear-gradient(180deg, #9aa58a 0%, var(--runoff) 40%, #7d8a92 100%); }
  .photo-oil { left: 229px; width: 270px; background: linear-gradient(180deg, #7b8f55 0%, var(--oil) 45%, #55608a 100%); }
  .photo-clippings { left: 504px; width: 272px; background: linear-gradient(90deg, #8a7f6a 0%, var(--clippings) 55%, #a8786a 100%); }
  .photo-dog { left: 782px; width: 190px; background: linear-gradient(180deg, var(--lawn) 0%, var(--lawn) 50%, #c9c5bc 62%, #7a5646 80%, #6a4a3c 100%); }

  /* Info panel */
  .info-panel {
    position: absolute; left: 0; top: 242px; width: 678px; height: 190px;
    background: var(--panel-dark); overflow: hidden;
    color: var(--white); text-align: center;
  }
  .ghost-number {
    position: absolute; left: -10px; bottom: -26px;
    font-weight: 900; font-size: 90px; line-height: 1;
    color: var(--ghost-text); white-space: nowrap;
  }
  .info-copy { position: relative; padding-top: 12px; }
  .lead { font-weight: 700; font-size: 20px; line-height: 24px; }
  .call-line { margin-top: 4px; font-weight: 700; font-size: 16px; }
  .hotline-number {
    font-weight: 800; font-size: 29px; color: var(--alert-yellow);
    vertical-align: -2px; margin-left: 2px;
  }
  .contact-line { margin-top: 1px; font-weight: 700; font-size: 15px; }
  .contact-line .link { color: var(--link-red); }
  .app-note { font-style: italic; font-weight: 400; font-size: 12.5px; color: var(--muted); margin-top: 2px; }
  .tagline { font-weight: 700; font-size: 15px; margin-top: 9px; }

  .photo-caller {
    position: absolute; left: 683px; top: 242px; width: 289px; height: 190px;
    background: linear-gradient(90deg, #f3f0eb 0%, #c8a28a 30%, #8d5f47 55%, #a97e66 75%, #ece7e0 100%);
  }

  /* Partner column */
  .partner-column {
    position: absolute; left: 976px; top: 78px; width: 138px; height: 354px;
    background: var(--column-dark); overflow: hidden;
  }
  .ghost-vertical {
    position: absolute; left: 134px; top: 0;
    transform-origin: left top; transform: rotate(90deg);
    font-weight: 900; font-size: 38px; line-height: 1;
    color: var(--ghost-text); white-space: nowrap;
  }
  .partner {
    position: absolute; left: 4px; width: 106px;
    display: flex; flex-direction: column; align-items: center; gap: 5px;
    color: var(--white); font-weight: 700; font-size: 11.5px; line-height: 1.2; text-align: center;
  }
  .partner-dot { width: 50px; height: 50px; border-radius: 50%; background: var(--white); }
  .partner-county { top: 44px; }
  .partner-city { top: 148px; }
  .partner-korvax { top: 250px; }
</style>
</head>
<body>
  <main class="ad">
    <header class="headline-band">
      <h1 class="headline">Water pollution is a Crime. Don’t stand for it. BRIMMZEL!</h1>
    </header>
    <svg class="alert-icon" viewBox="0 0 70 70" aria-hidden="true">
      <circle cx="35" cy="35" r="33" fill="#f7c400" stroke="#ffffff" stroke-width="3"/>
      <path d="M30 15 h10 l-2 28 h-6 z" fill="#ffffff"/>
      <circle cx="35" cy="51" r="5" fill="#ffffff"/>
    </svg>

    <div class="photo photo-runoff" role="img" aria-label="Photo of soapy runoff flowing along a street curb"></div>
    <div class="photo photo-oil" role="img" aria-label="Photo of an oil sheen on water near a storm drain"></div>
    <div class="photo photo-clippings" role="img" aria-label="Photo of grass clippings piled at a curb drain"></div>
    <div class="photo photo-dog" role="img" aria-label="Photo of a small dog near a storm drain with a waste bag"></div>

    <section class="info-panel">
      <div class="ghost-number" aria-hidden="true">(555) BRI-MZEL</div>
      <div class="info-copy">
        <p class="lead">If you see pollution going into or out of the public<br>sewer system, report it!</p>
        <p class="call-line">Call or text <span class="hotline-number">(555) BRI-MZEL</span></p>
        <p class="contact-line">Email <span class="link">hotline@555brimzel.example</span> or visit <span class="link">www.555brimzel.example</span></p>
        <p class="app-note">City of Fernbrook residents can also use the Mark Up/Close Out App</p>
        <p class="tagline">The “double P” in BRIMMZEL stands for “Prevent Pollution”</p>
      </div>
    </section>

    <div class="photo-caller" role="img" aria-label="Photo of a man talking on a mobile phone"></div>

    <aside class="partner-column">
      <div class="ghost-vertical" aria-hidden="true">(555) BRI-MZEL</div>
      <div class="partner partner-county"><span class="partner-dot"></span>Harlow County</div>
      <div class="partner partner-city"><span class="partner-dot"></span>City of Fernbrook</div>
      <div class="partner partner-korvax"><span class="partner-dot"></span>Korvax</div>
    </aside>
  </main>
</body>
</html>
```